Design PSD for eCommerce retail website
based on websites that we liked
Design PSD for eCommerce retail website - Retailers
Creative Brief
Retailers
Hi, We currently run a wholesale website http://www.corvettapursehouse.com and now we want a retail version of this so we can operate an eCommerce online shop website. We will sell exactly the same products as we have on the wholesale website, however with different price and targeting at consumers. So we want the website look dynamic, fresh and consumer-friendly. Currently our managers particularly picked a website they liked: - Home Page: http://soin.valmorique.com/en_fr/ - Product Listing Page: http://soin.valmorique.com/en_fr/shop/bougies/toutes?limit=all - Product Detail Page: http://soin.valmorique.com/en_fr/shop/bougies/bougies-parfumees/candied-fruits-candle We sells fashion bags as you can see from our wholesale website, and mainly targeting at girls and young ladies, but we also have a range of collections that target professionals, so please make sure the color, style and theme are just about right.
Hi, We currently run a wholesale website http://www.corvettapursehouse.com and now we want a retail version of this so we can operate an eCommerce online shop website. We will sell exactly the same products as we have on the wholesale website, however with different price and targeting at consumers. So we want the website look dynamic, fresh and consumer-friendly. Currently our managers particularly picked a website they liked: - Home Page: http://soin.valmorique.com/en_fr/ - Product Listing Page: http://soin.valmorique.com/en_fr/shop/bougies/toutes?limit=all - Product Detail Page: http://soin.valmorique.com/en_fr/shop/bougies/bougies-parfumees/candied-fruits-candle We sells fashion bags as you can see from our wholesale website, and mainly targeting at girls and young ladies, but we also have a range of collections that target professionals, so please make sure the color, style and theme are just about right. What we need now is similarly to the 3 pages above: - 1 Home page for the new eCommerce website - 1 Product listing page for the new website - 1 Product detail page for the new website
Colorful
Soft
Feminine
Light sky blue
pink
you decided
top
http://soin.valmorique.com/en_fr
http://soin.valmorique.com/en_fr/shop/bougies/toutes?limit=all
http://soin.valmorique.com/en_fr/shop/bougies/bougies-parfumees/candied-fruits-candle
qtorvan7 qtorvan7
Hi All, Please feel free to just submit 1 home page PSD design before continue working on other pages - I'll request your other pages if the home page is liked by our manager. Thank you.
Hi pulsor, thank you for the submission. The design is actually a bit too much colors and I feel like many pieces of elements are scrambled into one place - will you be able to copy the look and feel from http://soin.valmorique.com/en_fr/ please? This website is particularly selected by my manager so I guess if you can make a similar look and feel website for the fashion bags that would do the job. :) Many thanks again and I look forward to seeing your excellent work! Best Regards, Nerys

```html
<!DOCTYPE html>
<html lang="en">
<head>
<meta charset="utf-8">
<title>Corvetta Purse – What's New</title>
<link href="https://fonts.googleapis.com/css2?family=Roboto:wght@300;400;500;700&display=swap" rel="stylesheet">
<style>
  :root {
    --pink: #f4166f;
    --pink-deep: #e0105f;
    --canvas: #ebebeb;
    --white: #ffffff;
    --ink: #333333;
    --ink-soft: #444444;
    --ring: #dcdcdc;
    --shadow: rgba(0,0,0,0.18);
  }
  * { margin: 0; padding: 0; box-sizing: border-box; }
  html, body { width: 1200px; height: 732px; overflow: hidden; background: var(--canvas); }
  body { font-family: "Roboto", Arial, sans-serif; color: var(--ink); }

  .page { position: relative; width: 1200px; height: 732px; overflow: hidden; background: var(--canvas); }

  .band { position: absolute; inset: 0; }

  .brand {
    position: absolute; top: 38px; left: 0; width: 1272px; text-align: center;
    font-size: 24px; font-weight: 500; letter-spacing: 0.5px; color: var(--ink);
  }

  .main-nav { position: absolute; top: 152px; left: 0; list-style: none; }
  .main-nav li {
    position: absolute; height: 30px; line-height: 30px; font-size: 20px; color: var(--ink-soft);
    white-space: nowrap;
  }
  .main-nav li::before {
    content: ""; position: absolute; inset: 0 -10px 0 -14px; background: var(--white);
    transform: skewX(-22deg); z-index: -1;
  }
  .main-nav a { color: inherit; text-decoration: none; }

  .scroll-down {
    position: absolute; left: 55px; top: 463px; width: 106px; height: 106px; border-radius: 50%;
    background: var(--white); box-shadow: 0 4px 10px var(--shadow);
    display: flex; align-items: center; justify-content: center;
  }

  .intro { position: absolute; left: 272px; top: 300px; width: 300px; }
  .intro-title { font-size: 54px; font-weight: 300; color: var(--ink); line-height: 1; }
  .intro-title .accent { color: var(--pink); }
  .intro-text { margin-top: 32px; font-size: 15.5px; line-height: 21px; color: var(--ink); }

  .bubble {
    position: absolute; border-radius: 50%; background: var(--white);
    border: 2px solid var(--ring); box-shadow: 0 3px 8px rgba(0,0,0,0.08);
    display: flex; align-items: center; justify-content: center;
  }
  .bubble .photo { border-radius: 50%; }

  .thumb { width: 134px; height: 134px; }
  .thumb .photo { width: 96px; height: 96px; }
  .thumb-red { left: 670px; top: 245px; }
  .thumb-red .photo { background: radial-gradient(circle at 50% 55%, #a0283a 0 36%, #f4f4f4 62%); }
  .thumb-plum { left: 605px; top: 384px; }
  .thumb-plum .photo { background: radial-gradient(circle at 50% 55%, #2f2233 0 38%, #f4f4f4 64%); }
  .thumb-grey { left: 622px; top: 521px; }
  .thumb-grey .photo { background: radial-gradient(circle at 50% 55%, #5f605c 0 38%, #f4f4f4 64%); }

  .order-bubble { left: 797px; top: 178px; width: 134px; height: 134px; }
  .order-bubble .photo {
    position: absolute; inset: 18px; background: radial-gradient(circle at 50% 62%, #a88a76 0 32%, #f4f4f4 60%);
  }
  .order-badge {
    position: relative; width: 84px; height: 84px; border-radius: 50%; background: var(--pink);
    color: var(--white); font-size: 17px; font-weight: 700; display: flex; align-items: center; justify-content: center;
    margin-top: -22px;
  }

  .hero { left: 760px; top: 268px; width: 400px; height: 400px; border: 4px solid var(--ring); }
  .hero .photo {
    width: 360px; height: 360px;
    background: radial-gradient(ellipse 46% 40% at 50% 55%, #9a7a66 0 60%, #b79c8a 78%, #fafafa 100%);
  }

  .pager {
    position: absolute; left: 1020px; top: 221px; width: 120px; height: 120px; border-radius: 50%;
    background: var(--white); box-shadow: 0 4px 10px var(--shadow);
    display: flex; align-items: center; justify-content: center;
  }
</style>
</head>
<body>
<div class="page">
  <svg class="band" width="1200" height="732" viewBox="0 0 1200 732" aria-hidden="true">
    <polygon points="0,0 278,0 0,700" fill="var(--pink)"/>
    <polygon points="945,0 1200,0 1200,732 1155,732" fill="var(--pink)"/>
  </svg>

  <div class="brand">CORVETTA PURSE</div>

  <ul class="main-nav">
    <li style="left:120px;top:0"><a href="#">What's New</a></li>
    <li style="left:74px;top:43px"><a href="#">Union Jack bag</a></li>
    <li style="left:26px;top:85px"><a href="#">Leather Accessories</a></li>
    <li style="left:26px;top:130px"><a href="#">Handbags</a></li>
    <li style="left:74px;top:173px"><a href="#">Accessories</a></li>
    <li style="left:120px;top:215px"><a href="#">Sale</a></li>
  </ul>

  <div class="scroll-down" aria-label="Scroll down">
    <svg width="40" height="24" viewBox="0 0 40 24"><polyline points="4,4 20,19 36,4" fill="none" stroke="var(--ink)" stroke-width="4" stroke-linecap="round" stroke-linejoin="round"/></svg>
  </div>

  <section class="intro">
    <h1 class="intro-title"><span class="accent">Whats</span> New</h1>
    <p class="intro-text">Lorem Ipsum is simply dummy text of the printing and typesetting industry. Lorem Ipsum has been the industry's standard dummy text ever since the</p>
  </section>

  <div class="bubble thumb thumb-red"><div class="photo" role="img" aria-label="Red leather handbag"></div></div>
  <div class="bubble thumb thumb-plum"><div class="photo" role="img" aria-label="Dark plum slouch handbag"></div></div>
  <div class="bubble thumb thumb-grey"><div class="photo" role="img" aria-label="Grey structured handbag"></div></div>

  <div class="bubble order-bubble">
    <div class="photo" role="img" aria-label="Tan satchel bag"></div>
    <div class="order-badge">ORDER</div>
  </div>

  <div class="bubble hero"><div class="photo" role="img" aria-label="Brown leather satchel with buckled straps"></div></div>

  <div class="pager" aria-label="Previous and next">
    <svg width="70" height="40" viewBox="0 0 70 40"><polyline points="18,6 6,20 18,34" fill="none" stroke="var(--ink)" stroke-width="4" stroke-linecap="round" stroke-linejoin="round"/><polyline points="52,6 64,20 52,34" fill="none" stroke="var(--ink)" stroke-width="4" stroke-linecap="round" stroke-linejoin="round"/></svg>
  </div>
</div>
</body>
</html>
```